Varrow Business Card Design - Professional Flexible and forward thinking. Clean and Easy to follow

Management Consulting Company. I focus on business development and concept and operational review. I need a progressive, simple and professional layout design for the business cards, letterhead and envelops
Professional Flexible and forward thinking. Clean and Easy to follow
Mature Business persons and professionals and Corporations

Target Market(s)

Mature Business persons and professionals and Corporations - Government org.

Industry/Entity Type

Consulting

Contact Information for Business Card

Requirements
Must have
• Marcus Varrow
• President
• Phone - 347.682.1530
• email - Mvarrow@varrowpartners-example.com
• Skype - Marc.varrow
• 2187 Tollbrook Lane
• Suite A
• Massapequa, N.Y. 11492
• USA
Nice to have
• www.varrowpartners-example.com
Should not have
• N/A

```html
<!DOCTYPE html>
<html lang="en">
<head>
<meta charset="utf-8">
<title>Varrow Business Card Design</title>
<link href="https://fonts.googleapis.com/css2?family=Roboto+Condensed:wght@300;400;700&display=swap" rel="stylesheet">
<style>
  :root {
    --page: #ffffff;
    --card-grey: #3a3a3c;
    --ink-black: #000000;
    --accent: #f0592a;
    --text-light: #ffffff;
  }
  * { box-sizing: border-box; margin: 0; padding: 0; }
  html, body { width: 1200px; height: 1200px; overflow: hidden; background: var(--page); }
  body { position: relative; font-family: "Roboto Condensed", "Arial Narrow", sans-serif; }

  .card { position: absolute; left: 276px; width: 648px; height: 371px; overflow: hidden; }
  .card--front { top: 210px; background: var(--card-grey); }
  .card--back { top: 626px; background: var(--ink-black); }

  .brand-name {
    position: absolute; left: 40px; top: 36px;
    color: var(--text-light); font-weight: 300; line-height: 1.05;
    text-transform: uppercase; letter-spacing: 0.14em;
  }
  .brand-name__main { display: block; font-size: 52px; letter-spacing: 0.1em; margin-bottom: 4px; }
  .brand-name__sub { display: block; font-size: 23px; margin-left: 104px; }

  .divider-strip { position: absolute; left: 0; top: 158px; width: 100%; height: 7px; background: var(--ink-black); }
  .name-plate {
    position: absolute; left: 378px; top: 158px; width: 270px; height: 48px;
    background: var(--ink-black);
    color: var(--accent); font-weight: 700; font-size: 25px;
    text-align: right; padding: 9px 32px 0 0; text-transform: uppercase;
  }
  .role { position: absolute; right: 32px; top: 212px; color: var(--text-light); font-size: 26px; font-weight: 400; }

  .contacts { position: absolute; left: 40px; top: 180px; list-style: none; color: var(--text-light); font-size: 24px; line-height: 1.05; }
  .contacts li { display: flex; align-items: flex-start; margin-bottom: 8px; }
  .contacts .icon { width: 34px; height: 30px; margin-right: 12px; flex: none; }
  .contacts .at { color: var(--accent); }
  .website { position: absolute; left: 44px; top: 320px; color: var(--accent); font-size: 24px; }

  .address { position: absolute; right: 32px; top: 302px; color: var(--text-light); font-size: 21px; line-height: 1.5; text-align: left; }

  .back-name {
    position: absolute; inset: 0; display: flex; align-items: center; justify-content: center;
    color: var(--accent); font-weight: 300; font-size: 150px; letter-spacing: 0.08em; text-transform: uppercase;
  }
</style>
</head>
<body>
  <section class="card card--front">
    <div class="brand-name">
      <span class="brand-name__main">Varrow</span>
      <span class="brand-name__sub">Management</span>
      <span class="brand-name__sub">Consulting</span>
    </div>

    <div class="divider-strip"></div>
    <div class="name-plate">Marcus Varrow</div>
    <div class="role">President</div>

    <ul class="contacts">
      <li>
        <svg class="icon" viewBox="0 0 34 30" aria-hidden="true">
          <path fill="#f0592a" d="M7 3c2-1 3 0 4 2l2 5c0 2-1 3-2 4 1 3 4 6 7 7 1-1 2-2 4-2l5 2c2 1 2 3 1 4l-2 3c-2 2-6 1-11-3S2 14 3 9c0-2 2-5 4-6z"/>
        </svg>
        <span>347.682.1530</span>
      </li>
      <li>
        <svg class="icon" viewBox="0 0 34 30" aria-hidden="true">
          <rect x="1" y="8" width="32" height="22" fill="#f0592a"/>
          <path d="M2 9l15 12 15-12" fill="none" stroke="#3a3a3c" stroke-width="2.5"/>
        </svg>
        <span>Mvarrow<span class="at">@</span><br>varrowpartners-example.com</span>
      </li>
      <li>
        <svg class="icon" viewBox="0 0 34 30" aria-hidden="true">
          <circle cx="15" cy="15" r="13" fill="#f0592a"/>
        </svg>
        <span>Marc.varrow</span>
      </li>
    </ul>
    <div class="website">varrowpartners-example.com</div>

    <div class="address">2187 Tollbrook Lane, Suite A<br>Elmshaven, EH11492, USA</div>
  </section>

  <section class="card card--back">
    <div class="back-name">Varrow</div>
  </section>
</body>
</html>
```